PowerPoint Design Project

I need a Power Point slide template designed with 4 or 5 slides. We are a health care technology company and would like to take our current look and feel in this PP presentation to the next level and "prettied up"

Target Market(s)

Health Care Professionals

Industry/Entity Type

Health

Requirements
Must have
• Cannot change out the TREVONA logo. The logo is all CAPS
Should not have
• The color blue is restricted and cannot be used.

```html
<!DOCTYPE html>
<html lang="en">
<head>
<meta charset="utf-8">
<title>TREVONA Slide Template</title>
<link rel="stylesheet" href="https://fonts.googleapis.com/css2?family=Roboto:wght@400&display=swap">
<style>
  :root {
    --stage: #efefef;
    --paper: #ffffff;
    --ink: #3a3a3a;
    --rule: #141414;
    --steel-light: #e4e4e4;
    --steel-mid: #b4b4b4;
    --steel-dark: #7e7e7e;
    --brand-grey: #808080;
    --photo-warm: #d9cfc6;
    --photo-cool: #e3e6e7;
  }
  html, body { margin: 0; padding: 0; overflow: hidden; }
  body { width: 1200px; height: 658px; background: var(--stage); position: relative; font-family: "Roboto", Arial, sans-serif; }
  .slide { position: absolute; width: 362px; height: 280px; overflow: hidden; background: var(--paper); box-shadow: 0 2px 6px rgba(0,0,0,.25); }
  .col-1 { left: 26px; } .col-2 { left: 420px; } .col-3 { left: 814px; }
  .row-1 { top: 24px; } .row-2 { top: 354px; }

  /* content slides */
  .slide-header { position: absolute; left: 0; top: 0; width: 100%; height: 30px;
    background: linear-gradient(180deg, var(--steel-light), var(--steel-mid) 70%, var(--steel-dark));
    border-bottom: 3px solid var(--rule); }
  .slide-title { position: absolute; top: 3px; margin: 0; font-weight: 400; font-size: 22px; color: #fff; letter-spacing: .2px; }
  .title-right { right: 14px; } .title-left { left: 13px; }
  .slide-footer { position: absolute; left: 0; bottom: 0; width: 100%; height: 19px;
    background: linear-gradient(180deg, var(--steel-mid), var(--steel-dark));
    border-top: 2px solid var(--rule); }
  .photo { position: absolute; top: 33px; bottom: 21px; }
  .photo-left { left: 0; width: 150px; background: linear-gradient(90deg, var(--photo-warm), var(--photo-cool) 75%, rgba(255,255,255,0)); }
  .photo-right { right: 0; width: 190px; background: linear-gradient(270deg, var(--photo-cool), var(--photo-warm) 45%, rgba(255,255,255,0)); }
  .copy { position: absolute; font-size: 7.6px; line-height: 1.5; color: var(--ink); text-align: justify; }
  .copy p { margin: 0 0 7px; }
  .copy ul { margin: 0; padding: 0; list-style: none; }
  .copy li { position: relative; padding-left: 8px; margin-bottom: 3px; }
  .copy li::before { content: ""; position: absolute; left: 0; top: 4px; width: 3px; height: 3px; border-radius: 50%; background: var(--ink); }
  .copy-right { left: 150px; width: 199px; top: 76px; }
  .copy-narrow { left: 163px; width: 186px; top: 62px; }
  .copy-left { left: 14px; width: 199px; top: 70px; }
  .copy-list { left: 14px; width: 199px; top: 68px; text-align: left; }

  /* cover slides */
  .cover { background: linear-gradient(180deg, #cfcfcf, #a9a9a9 40%, #9a9a9a); }
  .cover-lower { position: absolute; left: 0; top: 194px; width: 100%; height: 86px; background: linear-gradient(180deg, #a4a4a4, #8d8d8d); }
  .emblem-art { position: absolute; left: 20px; top: 0; width: 180px; height: 280px;
    background: radial-gradient(ellipse at 50% 22%, rgba(255,255,255,.85), rgba(220,220,220,.5) 40%, rgba(160,160,160,0) 70%); }
  .brand-band { position: absolute; left: 0; top: 90px; width: 100%; height: 104px;
    background: linear-gradient(90deg, rgba(238,238,238,.88), #ececec 60%, #f3f3f3); }
  .brand-name { position: absolute; right: 30px; top: 34px; margin: 0; font-weight: 400; font-size: 32px; color: var(--brand-grey); }
  .thanks { position: absolute; right: 30px; bottom: 12px; margin: 0; font-weight: 400; font-size: 28px; color: #fff; }
</style>
</head>
<body>

  <section class="slide cover col-1 row-1">
    <div class="cover-lower"></div>
    <div class="emblem-art" role="img" aria-label="Silver winged medical staff emblem"></div>
    <div class="brand-band"><p class="brand-name">TREVONA</p></div>
  </section>

  <section class="slide col-2 row-1">
    <header class="slide-header"><h2 class="slide-title title-right">Introduction</h2></header>
    <div class="photo photo-left" role="img" aria-label="Smiling male doctor with stethoscope"></div>
    <div class="copy copy-right">
      <p>Lorem Ipsum is simply dummy text of the printing and typesetting industry. Lorem Ipsum has been the industry's standard dummy text ever since the 1500s, when an unknown printer took a galley of type and scrambled it to make a type specimen book.</p>
      <p>It has survived not only five centuries, but also the leap into electronic typesetting, remaining essentially unchanged. It was popularised in the 1960s with the release of Letraset sheets containing Lorem Ipsum passages, and more recently with desktop publishing software like Aldus PageMaker including versions of Lorem Ipsum.</p>
    </div>
    <footer class="slide-footer"></footer>
  </section>

  <section class="slide col-3 row-1">
    <header class="slide-header"><h2 class="slide-title title-left">Function</h2></header>
    <div class="photo photo-right" role="img" aria-label="Female doctor working at a computer"></div>
    <div class="copy copy-list">
      <p>Lorem Ipsum is simply dummy text of the printing and typesetting industry.</p>
      <ul>
        <li>It has survived not only five centuries</li>
        <li>Contrary to popular belief, Lorem Ipsum is not simply random text.</li>
        <li>discovered the undoubtable source. Lorem Ipsum comes from sections 1.10.32</li>
        <li>The standard chunk of Lorem Ipsum used since the 1500s is reproduced</li>
        <li>It is a long established fact that a reader will be distracted by the readable content of a page when looking at its layout.</li>
      </ul>
    </div>
    <footer class="slide-footer"></footer>
  </section>

  <section class="slide col-1 row-2">
    <header class="slide-header"><h2 class="slide-title title-right">Lorem Ipsum</h2></header>
    <div class="photo photo-left" role="img" aria-label="Nurse in scrubs writing on a clipboard"></div>
    <div class="copy copy-narrow">
      <p>Lorem Ipsum is simply dummy text of the printing and typesetting industry. Lorem Ipsum has been the industry's standard dummy text ever since the 1500s, when an unknown printer took a galley of type and scrambled it to make a type specimen book.</p>
      <p>It has survived not only five centuries, but also the leap into electronic typesetting, remaining essentially unchanged. It was popularised in the 1960s with the release of Letraset sheets containing Lorem Ipsum passages, and more recently with desktop publishing software like Aldus PageMaker including versions of Lorem Ipsum.</p>
    </div>
    <footer class="slide-footer"></footer>
  </section>

  <section class="slide col-2 row-2">
    <header class="slide-header"><h2 class="slide-title title-left">Team work</h2></header>
    <div class="photo photo-right" role="img" aria-label="Smiling female doctor with medical team behind"></div>
    <div class="copy copy-left">
      <p>Lorem Ipsum is simply dummy text of the printing and typesetting industry. Lorem Ipsum has been the industry's standard dummy text ever since the 1500s, when an unknown printer took a galley of type and scrambled it to make a type specimen book.</p>
      <p>It has survived not only five centuries, but also the leap into electronic typesetting, remaining essentially unchanged. It was popularised in the 1960s with the release of Letraset sheets containing Lorem Ipsum passages, and more recently with desktop publishing software like Aldus PageMaker including versions of Lorem Ipsum.</p>
    </div>
    <footer class="slide-footer"></footer>
  </section>

  <section class="slide cover col-3 row-2">
    <div class="cover-lower"></div>
    <div class="emblem-art" role="img" aria-label="Silver winged medical staff emblem"></div>
    <div class="brand-band"><p class="brand-name">TREVONA</p></div>
    <p class="thanks">Thank You</p>
  </section>

</body>
</html>
```